Boutique raw honey label from Australia. Blue mountains clean environment

I need a quirky Eco label for a raw honey product to appeal to boutique honey buyers with Gm free 100% raw honey included. Honey come from blue mountains a world heritage listed area in nsw Aust.
Want to appeal to people who love good food and love beautiful things and who want to know where there food comes from and how it is grown. Gm free, pesticide free, hand poured family run and owned business

Target Market(s)

Health conscious, lovers of fine food

Industry/Entity Type

Environment

Font styles to use
Other font styles liked:
• Courier

Requirements
Must have
• 100% Raw
Nice to have
• A little blurb about where honey is from
• # please see my current label - something similar to this but with a vintage bee design possibly

```html
<!DOCTYPE html>
<html lang="en">
<head>
<meta charset="utf-8">
<title>Wild Ridge Honey Co. – Raw Honey Label</title>
<link rel="stylesheet" href="https://fonts.googleapis.com/css2?family=Courier+Prime&family=Source+Sans+3:wght@300;700&display=swap">
<style>
  :root {
    --page-bg: #f1f1f1;
    --label-bg: #efebdf;
    --label-edge: #d9d3c2;
    --ink: #333130;
    --ink-soft: #4a4744;
    --art-dark: #5a5651;
    --art-light: #b9b3a6;
  }
  * { margin: 0; padding: 0; box-sizing: border-box; }
  html, body {
    width: 1200px;
    height: 1200px;
    overflow: hidden;
    background: var(--page-bg);
  }
  .canvas {
    position: relative;
    width: 1200px;
    height: 1200px;
  }
  .label {
    position: absolute;
    left: 50px;
    top: 260px;
    width: 1100px;
    height: 680px;
    background: var(--label-bg);
    border: 1px solid var(--label-edge);
    color: var(--ink);
  }
  .brand-name {
    position: absolute;
    top: 40px;
    left: 0;
    width: 100%;
    text-align: center;
    font-family: "Source Sans 3", sans-serif;
    font-weight: 700;
    font-size: 68px;
    letter-spacing: 1px;
    line-height: 1;
  }
  .product-title {
    position: absolute;
    left: 94px;
    top: 160px;
    font-family: "Source Sans 3", sans-serif;
    font-size: 80px;
    line-height: 1;
    letter-spacing: -1px;
  }
  .product-title .percent { font-weight: 300; }
  .product-title .raw { font-weight: 700; }
  .origin {
    position: absolute;
    left: 96px;
    top: 250px;
    font-family: "Source Sans 3", sans-serif;
    font-weight: 300;
    font-size: 42px;
    line-height: 1;
    color: var(--ink-soft);
  }
  .mountain-art {
    position: absolute;
    left: 790px;
    top: 165px;
    width: 200px;
    height: 125px;
    background: linear-gradient(180deg, var(--art-light) 0%, var(--art-dark) 70%);
  }
  .rule {
    position: absolute;
    left: 260px;
    width: 800px;
    height: 3px;
    background: var(--ink);
  }
  .rule-top { top: 330px; }
  .rule-bottom { top: 640px; }
  .bee-art {
    position: absolute;
    left: 30px;
    top: 395px;
    width: 215px;
    height: 150px;
    background: radial-gradient(ellipse at center, var(--art-dark) 0%, var(--art-light) 60%, var(--label-bg) 100%);
  }
  .blurb {
    position: absolute;
    left: 260px;
    top: 355px;
    width: 790px;
    font-family: "Courier Prime", "Courier New", monospace;
    font-size: 29px;
    line-height: 35px;
    text-align: justify;
  }
  .signature {
    position: absolute;
    left: 260px;
    top: 590px;
    font-family: "Courier Prime", "Courier New", monospace;
    font-size: 29px;
    line-height: 1;
  }
  .net-weight {
    position: absolute;
    left: 50px;
    top: 600px;
    font-family: "Courier Prime", "Courier New", monospace;
    font-size: 24px;
    line-height: 1;
  }
</style>
</head>
<body>
<main class="canvas">
  <section class="label">
    <h1 class="brand-name">WILD RIDGE HONEY CO.</h1>
    <h2 class="product-title"><span class="percent">100%</span> <span class="raw">RAW HONEY</span></h2>
    <p class="origin">from World Heritage Blue Mountains</p>
    <div class="mountain-art" role="img" aria-label="Vintage engraving of Blue Mountains cliffs and gum trees"></div>
    <div class="rule rule-top"></div>
    <div class="bee-art" role="img" aria-label="Vintage illustration of two honey bees beside honeycomb cells"></div>
    <p class="blurb">With the clean Blue Mountains as their home and a varietal seasonal diet, it’s no wonder our bees are buzzing! GM free, pesticide free and no sugars added. Minimum filtration keeps nutrients and enzymes intact... by leaving it raw, we keep it pure.</p>
    <p class="signature">Tom Harlow beekeeper Blue Mountains, NSW.</p>
    <p class="net-weight">430g/net</p>
    <div class="rule rule-bottom"></div>
  </section>
</main>
</body>
</html>
```